we can communicate on this, but i want to follow the approach we took on Pellow|Quint & Marsh but i feel the card front needs the black background and the platinum and gold logo. The back? I am open. we can use the same info from PQ&M. Velmora Point is an enhanced equity investment fund - basically a very exclusive boutique hedge fund that uses only stock options. very advanced things. hope you are interested

Contact Information for Business Card

Dr. Lewis T. Brennick, CFA
Scientifique de fusée financière
701.555.0143
LBdoc4490@mailvex.example

4817 Birch Hollow Way W.
West Fargo, ND 58099

No web site

Colors

Designer to choose colors to be used in the design.

Requirements
Nice to have
• I tend to prefer the most visible applications of the logo to include logo and name, the logo version with a black background and the gold and platinum components separated by the black. I see this working well for a single side (logo and name - this is card front to me).
• I am fairly open to other treatments on the reverse side with the data. To me, it makes sense to have a different color rendition of the logo on the reverse and it may be a muted black tone on tone or an oversized portion that would have spot UV. Or, the reverse may play with colors and layout
Should not have
• Other colors = no no
• Decorative font

```html
<!DOCTYPE html>
<html lang="en">
<head>
<meta charset="utf-8">
<title>Velmora Point — Business Cards</title>
<link rel="stylesheet" href="https://fonts.googleapis.com/css2?family=Source+Sans+3:wght@400;600;700&display=swap">
<style>
  :root {
    --backdrop: #d5d6d6;
    --card: #0b0b0b;
    --gloss: #1d1d1d;
    --gloss-text: #262626;
    --gold: #d4a62a;
    --text-muted: #8d8d8d;
    --white: #f4f4f4;
    --rule-grey: #5a5a5a;
  }
  * { box-sizing: border-box; margin: 0; padding: 0; }
  html, body {
    width: 1200px; height: 900px; overflow: hidden;
    background: var(--backdrop);
    font-family: "Source Sans 3", "Myriad Pro", sans-serif;
  }
  .stage { position: relative; width: 1200px; height: 900px; }
  .card {
    position: absolute;
    width: 560px; height: 320px;
    background: var(--card);
    box-shadow: 0 6px 18px rgba(0,0,0,0.28);
  }
  .card--front { left: 320px; top: 100px; }
  .card--back  { left: 320px; top: 480px; }

  /* Front: tone-on-tone spot UV mark */
  .front-mark {
    position: absolute; inset: 0;
    display: flex; flex-direction: column; align-items: center; justify-content: center;
    gap: 18px;
  }
  .front-mark__dot {
    width: 112px; height: 112px; border-radius: 50%;
    background: radial-gradient(circle at 35% 30%, #2e2e2e, var(--gloss) 70%);
  }
  .front-mark__name {
    font-size: 40px; font-weight: 700; letter-spacing: 1px;
    color: var(--gloss-text);
  }

  /* Back: details side */
  .brand {
    position: absolute; left: 40px; top: 62px;
    display: flex; align-items: center; gap: 14px;
  }
  .brand__dot {
    width: 52px; height: 52px; border-radius: 50%;
    background: var(--gold);
  }
  .brand__name {
    font-size: 27px; font-weight: 700; color: var(--white); letter-spacing: 0.5px;
  }

  .divider { position: absolute; top: 170px; height: 1px; }
  .divider--grey { left: 40px; width: 260px; background: var(--rule-grey); }
  .divider--gold { left: 300px; width: 220px; background: var(--gold); }

  .person { position: absolute; right: 40px; top: 118px; text-align: right; }
  .person__name {
    font-size: 19px; font-weight: 600; color: var(--gold); line-height: 1.1;
  }
  .person__cred { font-size: 13px; }
  .person__title { font-size: 12.5px; color: var(--text-muted); margin-top: 3px; }

  .contact {
    position: absolute; right: 40px; top: 190px;
    list-style: none; text-align: right;
    font-size: 13px; color: var(--text-muted); line-height: 20px;
  }
  .contact li { display: flex; justify-content: flex-end; align-items: center; gap: 6px; }
  .contact svg { width: 11px; height: 11px; flex: none; }

  .address {
    position: absolute; left: 40px; top: 214px;
    font-style: normal; font-size: 13px; color: var(--text-muted); line-height: 19px;
  }
</style>
</head>
<body>
<main class="stage">

  <section class="card card--front" aria-label="Card front">
    <div class="front-mark">
      <span class="front-mark__dot"></span>
      <span class="front-mark__name">Velmora Point</span>
    </div>
  </section>

  <section class="card card--back" aria-label="Card back">
    <div class="brand">
      <span class="brand__dot"></span>
      <span class="brand__name">Velmora Point</span>
    </div>

    <div class="divider divider--grey"></div>
    <div class="divider divider--gold"></div>

    <div class="person">
      <p class="person__name">Dr. Lewis T. Brennick<span class="person__cred">, CFA</span></p>
      <p class="person__title">Scientifique de fusée financière</p>
    </div>

    <ul class="contact">
      <li>701.555.0143
        <svg viewBox="0 0 12 12" aria-hidden="true"><rect x="3" y="0.5" width="6" height="11" rx="1.2" fill="none" stroke="var(--gold)" stroke-width="1.2"/><line x1="5" y1="9.5" x2="7" y2="9.5" stroke="var(--gold)" stroke-width="1"/></svg>
      </li>
      <li>LBdoc4490@mailvex.example
        <svg viewBox="0 0 12 12" aria-hidden="true"><rect x="0.5" y="2" width="11" height="8" fill="var(--gold)"/><polyline points="0.5,2 6,7 11.5,2" fill="none" stroke="var(--card)" stroke-width="1"/></svg>
      </li>
    </ul>

    <address class="address">
      4817 Birch Hollow Way W.<br>
      West Fargo, ND 58099
    </address>
  </section>

</main>
</body>
</html>
```